Loyalty card for customers

I would like logo an a section for 10 places, so I can advertise 10th float is free, our business is health and wellness we offer magnesium float, hyperbaric oxygen and infrared sauna

```html
<!DOCTYPE html>
<html lang="en">
<head>
<meta charset="utf-8">
<title>Tidewell Floats – Loyalty Card</title>
<link rel="stylesheet" href="https://fonts.googleapis.com/css2?family=Josefin+Sans:wght@300;600;700&family=Oswald:wght@400&family=IBM+Plex+Sans:wght@400&family=Quicksand:wght@700&family=Kalam:wght@700&display=swap">
<style>
  :root {
    --page-top: #ffffff;
    --page-bottom: #dcdcdc;
    --ocean-deep: #0b5f93;
    --ocean-mid: #1389c6;
    --ocean-shadow: #0a3a5c;
    --sky-band: #87c9e8;
    --bullet-text: #a9dcf2;
    --white: #ffffff;
    --ink: #0a0a0a;
    --trim: #e02a2a;
    --dash: #222222;
  }
  * { margin: 0; padding: 0; box-sizing: border-box; }
  html, body { width: 1200px; height: 1000px; overflow: hidden; }
  body {
    position: relative;
    background: linear-gradient(180deg, var(--page-top) 0%, var(--page-top) 18%, var(--page-bottom) 34%, var(--page-bottom) 100%);
    font-family: "Josefin Sans", sans-serif;
  }
  .card {
    position: absolute;
    left: 227px;
    width: 714px;
    height: 428px;
    overflow: hidden;
  }
  .card--front { top: 59px; background: var(--ocean-mid); }
  .card--back { top: 515px; background: var(--white); }

  .front__photo {
    position: absolute;
    inset: 0 0 76px 0;
    background:
      radial-gradient(ellipse 55% 45% at 70% 62%, var(--ocean-shadow) 0%, rgba(10,58,92,0) 70%),
      linear-gradient(160deg, var(--ocean-mid) 0%, var(--ocean-deep) 55%, #0c4f7a 100%);
  }
  .brand {
    position: absolute;
    left: 74px;
    top: 58px;
    color: var(--white);
    font-family: "Josefin Sans", sans-serif;
    font-weight: 600;
    font-size: 44px;
    line-height: 48px;
    letter-spacing: 6px;
  }
  .brand__subtitle {
    position: absolute;
    left: 119px;
    top: 158px;
    color: var(--white);
    font-family: "Oswald", sans-serif;
    font-size: 19px;
    letter-spacing: 2.4px;
  }
  .services {
    position: absolute;
    left: 88px;
    top: 241px;
    list-style: none;
    color: var(--bullet-text);
    font-family: "IBM Plex Sans", sans-serif;
    font-size: 19px;
    line-height: 29px;
    letter-spacing: 0.5px;
  }
  .services li::before { content: "• "; }
  .front__band {
    position: absolute;
    left: 0; right: 0; bottom: 0;
    height: 76px;
    background: var(--sky-band);
  }
  .contact {
    position: absolute;
    top: 366px;
    color: var(--ink);
    font-family: "Quicksand", sans-serif;
    font-weight: 700;
    font-size: 18px;
    letter-spacing: 1.3px;
  }
  .contact--web { left: 82px; }
  .contact--social { left: 436px; display: flex; align-items: center; gap: 10px; letter-spacing: 0.6px; }
  .contact__dot { width: 20px; height: 20px; border-radius: 50%; background: var(--ink); }

  .trim {
    position: absolute;
    left: 23px;
    top: 24px;
    width: 667px;
    height: 380px;
    border: 1px dashed var(--trim);
    pointer-events: none;
  }

  .stamps { position: absolute; left: 0; top: 0; }
  .free-label {
    position: absolute;
    left: 535px;
    top: 214px;
    width: 86px;
    text-align: center;
    color: var(--white);
    font-family: "Kalam", cursive;
    font-weight: 700;
    font-size: 24px;
    letter-spacing: 1px;
  }
  .back__band {
    position: absolute;
    left: 0; right: 0; bottom: 0;
    height: 101px;
    background: var(--ink);
    display: flex;
    align-items: center;
    justify-content: center;
    color: var(--white);
    font-family: "Josefin Sans", sans-serif;
    font-size: 19px;
    letter-spacing: 2.4px;
    padding-top: 4px;
  }
  .offer__light { font-weight: 300; }
  .offer__bold { font-weight: 700; margin-left: 8px; }
  .offer__bold sup { font-size: 10px; vertical-align: 8px; }
  .offer__end { margin-left: 20px; }
</style>
</head>
<body>
  <section class="card card--front">
    <div class="front__photo" role="img" aria-label="Photo of a relaxed guest floating in a softly lit float tank, tinted ocean blue"></div>
    <div class="brand">Tidewell<br>Floats</div>
    <div class="brand__subtitle">LOYALTY CARD</div>
    <ul class="services">
      <li>MAGNESIUM FLOAT</li>
      <li>HYPERBARIC OXYGEN</li>
      <li>INFRARED SAUNA</li>
    </ul>
    <div class="front__band"></div>
    <div class="contact contact--web">www.tidewellfloats.com</div>
    <div class="contact contact--social"><span class="contact__dot"></span>TidewellFloats</div>
    <div class="trim"></div>
  </section>

  <section class="card card--back">
    <svg class="stamps" width="714" height="428" viewBox="0 0 714 428">
      <g fill="none" stroke="var(--dash)" stroke-width="1.3" stroke-dasharray="4 3">
        <circle cx="132" cy="123" r="43"/>
        <circle cx="245" cy="123" r="43"/>
        <circle cx="355" cy="123" r="43"/>
        <circle cx="466" cy="123" r="43"/>
        <circle cx="578" cy="123" r="43"/>
        <circle cx="132" cy="229" r="43"/>
        <circle cx="245" cy="229" r="43"/>
        <circle cx="355" cy="229" r="43"/>
        <circle cx="466" cy="229" r="43"/>
      </g>
      <circle cx="578" cy="229" r="43" fill="var(--ink)"/>
    </svg>
    <div class="free-label">FREE</div>
    <div class="back__band">
      <span class="offer__light">ENJOY 9 FLOATS &amp;</span>
      <span class="offer__bold">GET 10<sup>TH</sup></span>
      <span class="offer__bold offer__end">FOR FREE</span>
    </div>
    <div class="trim"></div>
  </section>
</body>
</html>
```